CALDERA
I need double sided standard sized Business Card [3.5" x 2"]
Open to designers choice
Professional
Tavo Berendsky
PO BOX 7312
ELMRIDGE, CA 90388
tavo@qrd4.com
WWW.QRD4.COM
IF YOU NEED ANOTHER FILE .PDF, .JPG, ETC. PLEASE LET ME KNOW

```html
<!DOCTYPE html>
<html lang="en">
<head>
<meta charset="utf-8">
<title>Caldera Stationery</title>
<link href="https://fonts.googleapis.com/css2?family=Cinzel:wght@700&family=Open+Sans:wght@400;600;700&display=swap" rel="stylesheet">
<style>
  :root{
    --bg:#e6e4e1;
    --paper:#ffffff;
    --ink:#1b1b1b;
    --red:#c4161c;
    --red-dark:#7e0d10;
    --gold:#f2a01e;
    --grey:#8a8a8a;
    --faint:#f3e9e6;
  }
  *{box-sizing:border-box;margin:0;padding:0}
  html,body{width:1200px;height:869px;overflow:hidden;background:var(--bg)}
  body{position:relative;font-family:"Open Sans",Arial,sans-serif;color:var(--ink)}
  .sheet,.envelope,.card{position:absolute;background:var(--paper);box-shadow:0 3px 10px rgba(0,0,0,.18);overflow:hidden}
  .swoosh{position:absolute;left:0;bottom:0;width:100%;display:block}
  .brand{display:flex;align-items:center;gap:6px;font-family:"Cinzel",serif;font-weight:700;color:var(--red);letter-spacing:1px}
  .brand-dot{display:inline-block;border-radius:50%;background:var(--red)}
  .watermark{position:absolute;border-radius:50%;background:var(--faint)}

  /* fax sheet */
  .fax{left:60px;top:40px;width:340px;height:440px}
  .fax .brand{position:absolute;top:18px;left:50%;transform:translateX(-50%);font-size:15px}
  .fax .brand-dot{width:12px;height:12px}
  .fax-title{position:absolute;top:54px;right:26px;font-weight:700;font-size:12px}
  .fax-table{position:absolute;top:70px;left:26px;width:288px;border-collapse:collapse;font-size:7px}
  .fax-table td{border:1px solid var(--ink);height:16px;padding:0 4px;width:25%}
  .fax-table td.label{font-weight:600}
  .fax-checks{position:absolute;top:140px;left:26px;width:288px;display:flex;justify-content:space-between;font-size:6.5px}
  .fax-checks span::before{content:"";display:inline-block;width:6px;height:6px;border:1px solid var(--ink);margin-right:3px;vertical-align:-1px}
  .fax .watermark{left:90px;top:170px;width:160px;height:160px}

  /* letterhead */
  .letterhead{left:440px;top:40px;width:340px;height:440px}
  .letterhead .brand{position:absolute;top:18px;left:50%;transform:translateX(-50%);font-size:15px}
  .letterhead .brand-dot{width:12px;height:12px}
  .letterhead .watermark{left:80px;top:120px;width:180px;height:180px}

  /* envelope */
  .envelope{left:60px;top:530px;width:500px;height:250px}
  .envelope-flap{position:absolute;top:0;left:0;width:100%;height:60px;display:block}
  .envelope .brand{position:absolute;top:72px;left:24px;font-size:14px}
  .envelope .brand-dot{width:11px;height:11px}
  .envelope-name{position:absolute;right:56px;bottom:16px;font-family:"Cinzel",serif;font-weight:700;font-size:13px;line-height:16px;color:#fff;letter-spacing:2px}

  /* business cards */
  .card{width:350px;height:200px}
  .card-front{left:820px;top:120px;background:var(--ink)}
  .card-front .brand{position:absolute;top:72px;left:50%;transform:translateX(-50%);font-size:26px}
  .card-front .brand-dot{width:20px;height:20px}
  .card-front .web{position:absolute;top:116px;width:100%;text-align:center;color:#cfcfcf;font-size:8px;letter-spacing:3px}
  .card-back{left:820px;top:380px;background:var(--ink)}
  .card-back .person{position:absolute;top:24px;left:22px;color:#fff}
  .person-name{font-weight:700;font-size:14px}
  .person-role{font-size:8px;color:var(--gold);margin-top:2px}
  .contact{position:absolute;top:78px;left:22px;color:#e8e8e8;font-size:8px;line-height:13px;list-style:none}
  .card-back .brand{position:absolute;top:70px;right:22px;font-size:16px}
  .card-back .brand-dot{width:13px;height:13px}
</style>
</head>
<body>

  <section class="sheet fax">
    <div class="brand"><span class="brand-dot"></span>CALDERA</div>
    <div class="fax-title">FAX</div>
    <table class="fax-table">
      <tr><td class="label">To:</td><td></td><td class="label">From:</td><td></td></tr>
      <tr><td class="label">Fax:</td><td></td><td class="label">Phone:</td><td></td></tr>
      <tr><td class="label">Date:</td><td></td><td class="label">Pages:</td><td></td></tr>
      <tr><td class="label">Re:</td><td></td><td class="label">CC:</td><td></td></tr>
    </table>
    <div class="fax-checks"><span>Urgent</span><span>For Review</span><span>Please Comment</span><span>Please Reply</span><span>Recycle</span></div>
    <div class="watermark" role="img" aria-label="Faint brand emblem area"></div>
    <svg class="swoosh" viewBox="0 0 340 60" height="60" preserveAspectRatio="none">
      <path d="M0 30 C110 10 230 50 340 14 L340 60 L0 60 Z" fill="var(--red)"/>
      <path d="M0 26 C110 6 230 46 340 10" fill="none" stroke="var(--gold)" stroke-width="2"/>
      <path d="M0 44 C120 26 240 60 340 34 L340 60 L0 60 Z" fill="var(--red-dark)"/>
    </svg>
  </section>

  <section class="sheet letterhead">
    <div class="brand"><span class="brand-dot"></span>CALDERA</div>
    <div class="watermark" role="img" aria-label="Faint brand emblem area"></div>
    <svg class="swoosh" viewBox="0 0 340 60" height="60" preserveAspectRatio="none">
      <path d="M0 30 C110 10 230 50 340 14 L340 60 L0 60 Z" fill="var(--red)"/>
      <path d="M0 26 C110 6 230 46 340 10" fill="none" stroke="var(--gold)" stroke-width="2"/>
      <path d="M0 44 C120 26 240 60 340 34 L340 60 L0 60 Z" fill="var(--red-dark)"/>
    </svg>
  </section>

  <section class="envelope">
    <svg class="envelope-flap" viewBox="0 0 500 60" preserveAspectRatio="none">
      <path d="M0 0 H500 V30 C360 60 140 60 0 30 Z" fill="var(--ink)"/>
    </svg>
    <div class="brand"><span class="brand-dot"></span>CALDERA</div>
    <svg class="swoosh" viewBox="0 0 500 90" height="90" preserveAspectRatio="none">
      <path d="M0 40 C160 18 320 60 500 20 L500 90 L0 90 Z" fill="var(--red)"/>
      <path d="M0 35 C160 13 320 55 500 15" fill="none" stroke="var(--gold)" stroke-width="2"/>
    </svg>
    <div class="envelope-name">CALDERA</div>
  </section>

  <section class="card card-front">
    <div class="brand"><span class="brand-dot"></span>CALDERA</div>
    <div class="web">WWW.QRD4.COM</div>
    <svg class="swoosh" viewBox="0 0 350 40" height="40" preserveAspectRatio="none">
      <path d="M0 22 C120 4 240 36 350 10 L350 40 L0 40 Z" fill="var(--red)"/>
      <path d="M0 18 C120 0 240 32 350 6" fill="none" stroke="var(--gold)" stroke-width="1.5"/>
    </svg>
  </section>

  <section class="card card-back">
    <div class="person">
      <div class="person-name">Tavo Berendsky</div>
      <div class="person-role">President</div>
    </div>
    <ul class="contact">
      <li>PO BOX 7312</li>
      <li>ELMRIDGE, CA 90388</li>
      <li>Tel: (562) 555-0142</li>
      <li>tavo@qrd4.com</li>
      <li>WWW.QRD4.COM</li>
    </ul>
    <div class="brand"><span class="brand-dot"></span>CALDERA</div>
    <svg class="swoosh" viewBox="0 0 350 30" height="30" preserveAspectRatio="none">
      <path d="M0 18 C120 4 240 28 350 8 L350 30 L0 30 Z" fill="var(--red)"/>
      <path d="M0 14 C120 0 240 24 350 4" fill="none" stroke="var(--gold)" stroke-width="1.5"/>
    </svg>
  </section>

</body>
</html>
```